Athletic Director Business Card

I need a business card that is very appealing and shows my school logo and colours (red, white and black). We just finished changing our school logo and have sent the two logos we use and I have also sent the logo W that we also use. I'm not sure if combining them works but I thought I would send it anyway and let your creative juices flow. Looking for a simple but very luring design. It could have the different sports on it but I think doing something with the logo is probably the direction I would like to see as we offer 11 different sports and 22 different teams so that might get to busy. We have a long "Tradition of Excellence" and maybe that could be on the card. If you need to change to logo by shadowing it, or making it a two colour with a glow in it or what every you think would make it look fantastic give it a try as I'm open to different looks.

Target Market(s)

Parents of high school athletes, businesses throughout our city, principals.

Industry/Entity Type

School

Requirements
Must have
• Name of School - Ridgemont Valley High School or just Ridgemont Valley.
My Name - Marcus Holloway
Position - Athletic Director
Phone - 403-555-0147
Cell - 403-555-0183
Email - mkholloway@pvsd.ab.ca
Website - www.ridgemontvalleyathletics.com

```html
<!DOCTYPE html>
<html lang="en">
<head>
<meta charset="utf-8">
<title>Ridgemont Valley Athletics — Business Card</title>
<link rel="stylesheet" href="https://fonts.googleapis.com/css2?family=Arvo:wght@700&family=Lato:wght@400;700&display=swap">
<style>
  :root {
    --bg: #2b2b2b;
    --card-black: #0d0d0d;
    --card-white: #f4f4f4;
    --red: #c8202a;
    --grey: #8a8a8a;
    --light: #d9d9d9;
    --badge: #1c1c1c;
    --ink: #222222;
  }
  * { margin: 0; padding: 0; box-sizing: border-box; }
  html, body { width: 1200px; height: 997px; overflow: hidden; background: var(--bg); }
  .stage { position: relative; width: 1200px; height: 997px; }

  .card {
    position: absolute;
    width: 600px; height: 342px;
    border-radius: 20px;
    overflow: hidden;
    background: var(--card-black);
    box-shadow: 0 14px 30px rgba(0,0,0,.5);
  }

  /* Back of card */
  .card-back { left: 300px; top: 110px; }
  .mascot-art {
    position: absolute; left: 170px; top: 40px;
    width: 300px; height: 210px; border-radius: 10px;
    background: linear-gradient(120deg, #6a1015 0%, #c8202a 55%, #d9d9d9 100%);
    opacity: .9;
  }
  .website {
    position: absolute; left: 0; right: 0; bottom: 30px; text-align: center;
    font-family: 'Arvo', serif; font-weight: 700; font-size: 16px; letter-spacing: .5px;
    color: var(--light); white-space: nowrap;
  }
  .website .accent { color: var(--red); }

  /* Front of card */
  .card-front { left: 300px; top: 520px; }
  .front-top { position: absolute; left: 0; top: 0; width: 100%; height: 150px; background: var(--card-white); }
  .monogram {
    position: absolute; left: 24px; top: 18px;
    font-family: 'Arvo', serif; font-weight: 700; font-size: 28px; color: var(--red);
  }
  .team-badge {
    position: absolute; left: 96px; top: 62px; width: 170px; height: 170px;
    border-radius: 50%; background: var(--badge); border: 5px solid var(--grey);
    display: flex; align-items: center; justify-content: center;
  }
  .team-name { font-family: 'Arvo', serif; font-weight: 700; font-size: 24px; color: var(--red); }
  .person { position: absolute; right: 24px; top: 112px; text-align: right; }
  .person-name { font-family: 'Arvo', serif; font-weight: 700; font-size: 18px; color: var(--red); letter-spacing: .5px; line-height: 1.3; }
  .person-title { font-family: 'Lato', sans-serif; font-size: 12px; color: var(--light); line-height: 1.6; }
  .contact {
    position: absolute; font-family: 'Lato', sans-serif; font-size: 15px; color: var(--light);
    display: flex; align-items: center; gap: 8px; white-space: nowrap;
  }
  .contact svg { width: 14px; height: 14px; fill: none; stroke: var(--light); stroke-width: 1.6; }
  .contact-email { right: 24px; top: 196px; font-size: 13px; }
  .contact-email .accent { color: var(--red); }
  .school-name {
    position: absolute; left: 24px; top: 250px;
    font-family: 'Arvo', serif; font-weight: 700; font-size: 18px; letter-spacing: .5px; color: var(--red); white-space: nowrap;
  }
  .school-name .white { color: #fff; }
  .contact-phone { left: 24px; top: 290px; }
  .contact-cell { left: 300px; top: 290px; }
</style>
</head>
<body>
<main class="stage">
  <section class="card card-back">
    <div class="mascot-art" role="img" aria-label="Large red and white hawk head mascot illustration"></div>
    <p class="website">WWW.<span class="accent">RIDGEMONTVALLEYATHLETICS</span>.COM</p>
  </section>

  <section class="card card-front">
    <div class="front-top"></div>
    <div class="monogram">RV</div>
    <div class="team-badge"><span class="team-name">RIDGECATS</span></div>
    <div class="person">
      <p class="person-name">MARCUS HOLLOWAY</p>
      <p class="person-title">Athletic Director</p>
    </div>
    <p class="contact contact-email">
      <svg viewBox="0 0 14 14"><rect x="1" y="3" width="12" height="8"/><path d="M1 3l6 5 6-5"/></svg>
      <span><span class="accent">mkholloway</span>@pvsd.ab.ca</span>
    </p>
    <p class="school-name">RIDGEMONT VALLEY <span class="white">HIGH SCHOOL</span></p>
    <p class="contact contact-phone">
      <svg viewBox="0 0 14 14"><path d="M2 5c0-2 10-2 10 0v1H9V5H5v1H2z"/><rect x="3" y="7" width="8" height="5"/></svg>
      403-555-0147
    </p>
    <p class="contact contact-cell">
      <svg viewBox="0 0 14 14"><rect x="4" y="1" width="6" height="12" rx="1"/></svg>
      403-555-0183
    </p>
  </section>
</main>
</body>
</html>
```